Poster

I need a poster for my business, www.coastaltablejourneysbay.example which some information about the most important activities (Sangria Tasting, Iberian Ham, Charcuteries & Sherry Wine Tasting, Sailboat Experiences and Picnic Experiences). A3 Format. Social media included (@coastaltablejourneyctj), contact information included.

```html
<!DOCTYPE html>
<html lang="en">
<head>
<meta charset="UTF-8">
<title>Coastal Table Journeys Bay – Poster</title>
<link href="https://fonts.googleapis.com/css2?family=Montserrat:wght@300;400;700&family=Oswald:wght@500&display=swap" rel="stylesheet">
<style>
  :root {
    --paper: #ffffff;
    --amber: #e89d20;
    --amber-light: #eca62b;
    --charcoal: #454141;
    --charcoal-light: #4c4848;
    --ink: #3e3a39;
    --text-light: #ffffff;
    --photo-olive: #3a2a1c;
    --photo-sea: #c9b49a;
  }
  * { margin: 0; padding: 0; box-sizing: border-box; }
  html, body { width: 900px; height: 1200px; overflow: hidden; }
  body {
    background: var(--paper);
    font-family: "Montserrat", sans-serif;
    position: relative;
  }
  .poster { position: absolute; inset: 0; background: var(--paper); }
  .panel {
    position: absolute; left: 43px; top: 41px; width: 814px; height: 1119px;
    overflow: hidden;
  }
  .panel-shapes { position: absolute; inset: 0; }
  .brand-ribbon { position: absolute; left: 453px; top: 0; width: 317px; height: 224px; }
  .brand {
    position: absolute; left: 478px; top: 56px; width: 270px;
    display: flex; align-items: center; gap: 14px;
  }
  .brand-mark { width: 26px; height: 26px; background: var(--amber); flex: none; }
  .brand-name {
    font-family: "Oswald", sans-serif; font-weight: 500; font-size: 27px;
    line-height: 1.1; color: var(--ink); text-transform: uppercase;
  }
  .activities {
    position: absolute; left: 65px; top: 88px; color: var(--text-light);
  }
  .activity { margin-bottom: 18px; font-size: 56px; line-height: 72px; }
  .activity b { font-weight: 700; }
  .activity span { font-weight: 300; }
  .photo { position: absolute; }
  .photo-picnic { left: 584px; top: 480px; width: 230px; height: 237px; }
  .photo-tapas { left: 453px; top: 522px; width: 195px; height: 148px; }
  .contact {
    position: absolute; left: 0; right: 0; top: 930px;
    text-align: center; color: var(--text-light);
  }
  .phone { font-weight: 300; font-size: 56px; line-height: 1; letter-spacing: 1px; }
  .website { margin-top: 26px; font-weight: 400; font-size: 28px; }
  .website strong { color: var(--amber); font-weight: 700; }
  .social {
    margin-top: 26px; font-weight: 400; font-size: 22px;
    display: flex; justify-content: center; align-items: center; gap: 12px;
  }
  .social-dot { width: 30px; height: 30px; border-radius: 50%; background: var(--amber); }
</style>
</head>
<body>
<div class="poster">
  <div class="panel">
    <svg class="panel-shapes" width="814" height="1119" viewBox="0 0 814 1119">
      <rect width="814" height="1119" fill="var(--amber)"/>
      <polygon points="0,0 330,0 550,1119 0,1119" fill="var(--amber-light)"/>
      <polygon points="0,908 814,765 814,1119 0,1119" fill="var(--charcoal)"/>
      <polygon points="500,820 814,765 814,1119 550,1119" fill="var(--charcoal-light)"/>
    </svg>

    <svg class="brand-ribbon" viewBox="0 0 317 224">
      <polygon points="0,0 317,0 317,224 160,173 0,224" fill="var(--paper)"/>
    </svg>
    <div class="brand">
      <div class="brand-mark"></div>
      <div class="brand-name">Coastal Table<br>Journeys Bay</div>
    </div>

    <div class="activities">
      <p class="activity"><b>Sangria</b><br><span>Tasting</span></p>
      <p class="activity"><b>Iberian</b> <span>Ham,</span><br><b>Charcuteries</b> <span>&amp; Sherry</span><br><b>Wine</b> <span>Tasting</span></p>
      <p class="activity"><b>Sailboat</b><br><span>Experiences</span></p>
      <p class="activity"><b>Picnic</b><br><span>Experiences</span></p>
    </div>

    <svg class="photo photo-picnic" viewBox="0 0 230 237" role="img" aria-label="Photo of a picnic basket with bread, wine and croissants on a blanket by the sea">
      <defs>
        <linearGradient id="picnicTone" x1="0" y1="0" x2="0" y2="1">
          <stop offset="0" stop-color="#9fb2c2"/>
          <stop offset="0.45" stop-color="var(--photo-sea)"/>
          <stop offset="1" stop-color="#8a5a34"/>
        </linearGradient>
      </defs>
      <polygon points="0,0 230,0 230,237 40,237 30,180 0,170" fill="url(#picnicTone)"/>
    </svg>

    <svg class="photo photo-tapas" viewBox="0 0 195 148" role="img" aria-label="Photo of a glass of green olives and tapas on a dark table">
      <defs>
        <linearGradient id="tapasTone" x1="0" y1="0" x2="1" y2="1">
          <stop offset="0" stop-color="#6b5a44"/>
          <stop offset="1" stop-color="var(--photo-olive)"/>
        </linearGradient>
      </defs>
      <polygon points="0,0 195,0 175,148 20,148" fill="url(#tapasTone)"/>
    </svg>

    <div class="contact">
      <p class="phone">+34 611 20 48 35</p>
      <p class="website">www.<strong>coastaltablejourneysbay</strong>.example</p>
      <p class="social"><span class="social-dot"></span>@coastaltablejourneyctj</p>
    </div>
  </div>
</div>
</body>
</html>
```